Tarek & Lubna's 50th Anniversary Celebration & Reunion

I need a flyer to send out via email and for posting on chatterboard to invite guests to a 50th wedding anniversary / family reunion.

Location is sunny La Jolla CA the Pearl of San Diego's Shore.

Week long daily activities starting Mon July 28-Aug 1st Friday, The event will be on Wednesday.
* Daily Catered Family Breakfast at the Marlow Hall of La Jolla
* Daily group activities including
*Exploring La Jolla Beaches & Ocean Cave Kayaking
*TideRealm Private Behind the Scenes Tour
*World Famous Pellham Wildlife Park
*Sunset Balloon Ride
*Private Yatch on the Bay

Actual Anniversary event will take place Thursday December 28, 2013 at 5pm at the Marlow Hall.

There are many local hotels around the Marlow Hall. 4213 Brindle Ln, La Jolla, CA 92058

Host is Kamil and the entire Haddour Family. For questions, please email Kamil@thelinden-feasts.com

Target Market(s)

all ages from 10 year olds to 70 year olds. Should appeal to all

Industry/Entity Type

Wedding

Font styles to use
Script

Colors

Designer to choose colors to be used in the design.

Requirements
Must have
• Fun graphics, including one with a stretch limo as there will be one available

Photo enclosed
Nice to have
• Logo for TideRealm Inserting a picture of an actual wedding 50 years ago or so of the bride and groom. incorporating the limo cropped out of the picture attached would also be nice

```html
<!DOCTYPE html>
<html lang="en">
<head>
<meta charset="utf-8">
<title>Tarek &amp; Lubna's 50th Anniversary Celebration &amp; Reunion</title>
<link rel="stylesheet" href="https://fonts.googleapis.com/css2?family=Damion&family=Kaushan+Script&display=swap">
<style>
  :root {
    --lime: #ccff66;
    --frame-blue: #0000ff;
    --title-cyan: #33ccff;
    --body-violet: #9966ff;
    --limo-dark: #5a5a7a;
    --limo-light: #a9a9c8;
  }
  html, body {
    margin: 0;
    padding: 0;
    overflow: hidden;
  }
  .flyer {
    position: relative;
    width: 1200px;
    height: 999px;
    background: var(--lime);
    overflow: hidden;
  }
  .flyer__frame {
    position: absolute;
    left: 0;
    top: 0;
  }
  .flyer__title {
    position: absolute;
    top: 136px;
    left: 0;
    width: 1200px;
    margin: 0;
    text-align: center;
    font-family: "Damion", cursive;
    font-weight: 400;
    font-size: 48px;
    line-height: 1.2;
    color: var(--title-cyan);
    transform: scaleX(0.56);
    white-space: nowrap;
  }
  .flyer__line {
    position: absolute;
    left: 120px;
    margin: 0;
    font-family: "Kaushan Script", cursive;
    font-size: 20px;
    line-height: 1;
    color: var(--body-violet);
    white-space: nowrap;
  }
  .flyer__limo {
    position: absolute;
    left: 780px;
    top: 420px;
    width: 300px;
    height: 120px;
    border-radius: 18px;
    background: linear-gradient(180deg, var(--limo-light), var(--limo-dark));
  }
</style>
</head>
<body>
<main class="flyer">
  <svg class="flyer__frame" width="1200" height="999" viewBox="0 0 1200 999" aria-hidden="true">
    <rect x="21" y="85" width="1158" height="827" rx="150" ry="150"
          fill="none" stroke="var(--frame-blue)" stroke-width="14"/>
  </svg>

  <h1 class="flyer__title">Tarek &amp; Lubna's 50th Anniversary Celebration &amp; Reunion</h1>

  <p class="flyer__line" style="top:260px">Location is sunny La Jolla CA the Pearl of San Diego's Shore</p>
  <p class="flyer__line" style="top:334px">Week long daily activities starting Mon July 29-Aug 1st Friday, The event will be on Wednesday.</p>

  <p class="flyer__line" style="top:407px">*Daily Catered Family Breakfast at the Marlow Hall of La Jolla</p>
  <p class="flyer__line" style="top:441px">*Daily group activities Includung</p>
  <p class="flyer__line" style="top:475px">*Exploring La Jolla Beaches &nbsp;&amp; ocean Cave Kayaking</p>
  <p class="flyer__line" style="top:509px">*TideRealm Private Behind the Scenes Tour</p>
  <p class="flyer__line" style="top:543px">*World Famous Pellham Wildlife Park</p>
  <p class="flyer__line" style="top:577px">*Sunset Balloon Ride</p>
  <p class="flyer__line" style="top:611px">*Private Yatch on the Bay</p>

  <div class="flyer__limo" role="img" aria-label="Illustration of the stretch limousine available to guests"></div>

  <p class="flyer__line" style="top:667px">Actual Anniversary event will take place Thursday December 28, 2013 at 5pm at the Marlow Hall</p>
  <p class="flyer__line" style="top:740px">There are many local hotels around the Marlow Hall. 4213 Brindle Ln , La Jolla , CA 92058</p>
  <p class="flyer__line" style="top:813px">host is Kamil and entire &nbsp;Haddour Family</p>
  <p class="flyer__line" style="top:848px">For questions, please email Kamil@thelinden-feasts.com</p>
</main>
</body>
</html>
```